Heavy diesel repair business requiring a capability statement to send out to potential new clients

We need a capability statement design to attract new clients, we are a mobile heavy diesel repair business that caters to mining, quarrying and transport industries. the main focus of this 3-4 page flyer is to show new clients our main capabilities and services we can provide

Company overview:
Here at Hallwick Diesel, we pride ourselves on providing end to end maintenance solutions focused on safety while meeting strict deadlines. With 20 years’ experience in the earthmoving and quarrying industry concentrating on downtime, process improvement, quality control and preventative maintenance our team have the skills to carry out any project safely and on time.
Our previous experience includes planned, project and breakdown maintenance for key players in the construction industry which own and operate quarries across multiple sites with fixed crushing plants, sand washing plants and concrete plants supported by a fleet of earthmoving equipment and road transport fleet.

Main capabilities:
Field service ( Preventative maintenance and servicing. Breakdowns, Diagnose and repair electrical faults with scan tools. Hydraulic faults. screen media change outs, conveyor belt and roller changes)

Component overhauls ( Engine rebuilds, transmission and final drive rebuilds, hydraulic cylinder reseals, sand pump overhauls, crusher component changes)

Inspections( Pre purchase inspections, BTQLM inspection and reports, wear components and media inspections)

Air conditioning ( Diagnose, service and replacement of all air conditioning components including end of life reclaim and destruction)

Line boring (On site line boring including supply and install of pins and bushes)

Fabrication ( Heavy fabrication repairs, and hard facing of buckets, rippers and shredders. Fabrication and repairs to fixed plant conveyors, screens and crushers)

Process improvements ( High wear areas, bottle necks, specific gradings and upgrades)

Target Market(s)

Earthmoving companies, quarries, mining and transport

Industry/Entity Type

Heavy diesel mechanical repair,

Requirements
Must have
• Company overview, why choose us, main capabilities, contact details
Nice to have
• 3-4 page flyer, company logo and colour scheme, background pictures and highlighted pictures

```html
<!DOCTYPE html>
<html lang="en">
<head>
<meta charset="utf-8">
<title>Hallwick Diesel – Capability Statement</title>
<link rel="stylesheet" href="https://fonts.googleapis.com/css2?family=Archivo+Black&family=Poppins:wght@300;400;500;700;800&display=swap">
<style>
  :root{
    --red:#e30613;
    --ink:#111111;
    --paper:#f1f1f1;
    --dark:#141414;
    --muted:#5a5a5a;
    --rule:#c9c9c9;
    --bg:#dcdcdc;
  }
  *{box-sizing:border-box;margin:0;padding:0}
  html,body{width:898px;height:1200px;overflow:hidden;background:var(--bg);font-family:"Poppins",sans-serif;color:var(--ink)}
  .spread{position:absolute;left:39px;width:820px;height:580px;display:flex;box-shadow:0 6px 18px rgba(0,0,0,.18)}
  .spread--covers{top:13px}
  .spread--inside{top:607px}
  .page{position:relative;width:410px;height:580px;overflow:hidden;background:var(--paper)}
  .page--dark{background:linear-gradient(160deg,#2a2522 0%,#161412 55%,#0c0c0c 100%);color:#fff}
  .photo{position:absolute;display:block}
  .brand{position:absolute;display:flex;align-items:center;gap:6px;font-weight:800;text-transform:uppercase;letter-spacing:.02em;line-height:1}
  .brand__dot{width:12px;height:12px;border-radius:50%;background:var(--red);flex:none}
  .brand__name{display:flex;flex-direction:column}
  .brand__name small{font-size:.55em;font-weight:800;letter-spacing:.08em}

  /* back cover */
  .back-photo{left:0;top:0;width:410px;height:300px}
  .contact{position:absolute;left:40px;top:460px;font-size:9px;line-height:1}
  .contact li{list-style:none;display:flex;align-items:center;gap:8px;margin-bottom:7px}
  .contact li:first-child{font-size:15px;font-weight:700}
  .contact svg{width:11px;height:11px;flex:none}
  .divider{position:absolute;left:240px;top:462px;width:1px;height:48px;background:var(--ink);transform:rotate(20deg)}
  .back-brand{left:268px;top:474px;font-size:16px;color:var(--ink)}

  /* front cover */
  .front-brand{left:180px;top:42px;font-size:26px;color:var(--ink)}
  .front-brand .brand__dot{width:26px;height:26px}
  .front-photo{left:0;top:120px;width:410px;height:320px}
  .cover-title{position:absolute;left:40px;top:380px;line-height:1}
  .cover-title__kicker{font-family:"Archivo Black",sans-serif;font-size:17px;letter-spacing:.02em}
  .cover-title__main{font-family:"Archivo Black",sans-serif;font-size:66px;letter-spacing:-.01em;margin-top:2px}
  .cover-title__sub{font-family:"Archivo Black",sans-serif;font-size:20px;color:var(--red);margin-top:4px}
  .pill{position:absolute;left:40px;top:510px;background:var(--red);color:#fff;font-weight:700;font-size:11px;padding:6px 22px;border-radius:20px}

  /* overview */
  .overview-title{position:absolute;left:30px;top:330px;transform:rotate(-90deg);transform-origin:left top;line-height:.95;white-space:nowrap}
  .overview-title__small{font-size:34px;font-weight:500;letter-spacing:.04em;color:#fff}
  .overview-title__big{font-size:60px;font-weight:500;letter-spacing:.02em;color:var(--red)}
  .overview-copy{position:absolute;left:200px;top:88px;width:185px;font-size:8.6px;line-height:1.42;font-weight:300}
  .overview-copy p+p{margin-top:10px}
  .footer-brand{font-size:12px}
  .page--dark .footer-brand{left:26px;top:512px;color:#fff}
  .footer-bar{position:absolute;height:5px;background:var(--red)}
  .footer-url{position:absolute;font-size:6.5px;color:var(--red)}
  .folio{position:absolute;font-size:7px;padding:1px 6px}

  /* capabilities */
  .cap-title{position:absolute;left:34px;top:34px;font-size:25px;font-weight:400}
  .cap-intro{position:absolute;left:34px;top:72px;width:340px;font-size:9px;line-height:1.35}
  .cap-grid{position:absolute;left:34px;top:130px;width:342px;display:grid;grid-template-columns:1fr 1fr;column-gap:16px;font-size:7px;line-height:1.35}
  .cap-col{display:flex;flex-direction:column}
  .cap-col:first-child{border-right:1px solid var(--rule);padding-right:12px}
  .cap-item{padding:9px 0;border-bottom:1px solid var(--rule)}
  .cap-item:last-child{border-bottom:0}
  .cap-photo{left:0;top:350px;width:410px;height:170px}
  .page--light .footer-brand{left:30px;top:534px;color:var(--ink)}
</style>
</head>
<body>

<section class="spread spread--covers">
  <!-- back cover -->
  <article class="page page--back">
    <svg class="photo back-photo" viewBox="0 0 410 300" role="img" aria-label="Photo of an excavator silhouetted against a dusk sky">
      <defs>
        <linearGradient id="dusk" x1="0" y1="0" x2="0" y2="1">
          <stop offset="0" stop-color="#1c1d22"/>
          <stop offset=".55" stop-color="#3a2a22"/>
          <stop offset=".8" stop-color="#5b3a24"/>
          <stop offset="1" stop-color="#15130f"/>
        </linearGradient>
      </defs>
      <path d="M0 0 H300 Q360 110 410 300 Q200 250 0 250 Z" fill="url(#dusk)"/>
    </svg>
    <ul class="contact">
      <li><svg viewBox="0 0 12 12"><circle cx="6" cy="6" r="6" fill="#e30613"/><path d="M4 3l1 1.4-.6.8c.4.9 1 1.5 1.9 1.9l.8-.6L8.5 7.5 7.8 9C5.3 8.7 3.3 6.7 3 4.2Z" fill="#fff"/></svg>0412 555 018</li>
      <li><svg viewBox="0 0 12 12"><circle cx="6" cy="6" r="6" fill="#e30613"/><rect x="3" y="4" width="6" height="4" fill="none" stroke="#fff" stroke-width=".8"/><path d="M3 4l3 2.3L9 4" fill="none" stroke="#fff" stroke-width=".8"/></svg>hallwickdiesel@mailbox.com</li>
      <li><svg viewBox="0 0 12 12"><circle cx="6" cy="6" r="6" fill="#e30613"/><circle cx="6" cy="6" r="3" fill="none" stroke="#fff" stroke-width=".8"/><path d="M3 6h6M6 3v6" stroke="#fff" stroke-width=".6"/></svg>www.yourwebsite.com</li>
    </ul>
    <span class="divider"></span>
    <div class="brand back-brand"><span class="brand__dot"></span><span class="brand__name">Hallwick<small>Diesel Pty Ltd</small></span></div>
  </article>

  <!-- front cover -->
  <article class="page page--front">
    <div class="brand front-brand"><span class="brand__dot"></span><span class="brand__name">Hallwick<small>Diesel Pty Ltd</small></span></div>
    <svg class="photo front-photo" viewBox="0 0 410 320" role="img" aria-label="Photo of a yellow wheel loader on a gravel site at sunset">
      <defs>
        <linearGradient id="sunset" x1="0" y1="0" x2="0" y2="1">
          <stop offset="0" stop-color="#e9b06a"/>
          <stop offset=".4" stop-color="#c98a4a"/>
          <stop offset=".65" stop-color="#7a5a3c"/>
          <stop offset="1" stop-color="#3e2e24"/>
        </linearGradient>
      </defs>
      <path d="M150 40 Q280 10 410 0 V320 H330 Q260 170 150 40 Z" fill="url(#sunset)"/>
    </svg>
    <div class="cover-title">
      <div class="cover-title__kicker">HEAVY DIESEL</div>
      <div class="cover-title__main">REPAIR</div>
      <div class="cover-title__sub">CAPABILITY STATEMENT</div>
    </div>
    <div class="pill">www.yourwebsite.com</div>
  </article>
</section>

<section class="spread spread--inside">
  <!-- company overview -->
  <article class="page page--dark" role="img" aria-label="Dark background photo of earthmoving machinery">
    <h2 class="overview-title">
      <span class="overview-title__small">COMPANY</span><br>
      <span class="overview-title__big">OVERVIEW</span>
    </h2>
    <div class="overview-copy">
      <p>Here at Hallwick Diesel, we pride ourselves on providing end to end maintenance solutions focused on safety while meeting strict deadlines. With 20 years’ experience in the earthmoving and quarrying industry concentrating on downtime, process improvement, quality control and preventative maintenance our team have the skills to carry out any project safely and on time.</p>
      <p>Our previous experience includes planned, project and breakdown maintenance for key players in the construction industry which own and operate quarries across multiple sites with fixed crushing plants, sand washing plants and concrete plants supported by a fleet of earthmoving equipment and road transport fleet.</p>
    </div>
    <div class="brand footer-brand"><span class="brand__dot"></span><span class="brand__name">Hallwick<small>Diesel Pty Ltd</small></span></div>
    <span class="footer-bar" style="left:130px;top:520px;width:270px"></span>
    <span class="footer-url" style="left:300px;top:540px">www.yourwebsite.com</span>
    <span class="folio" style="left:392px;top:556px;color:#fff">1</span>
  </article>

  <!-- main capabilities -->
  <article class="page page--light">
    <h2 class="cap-title">Main capabilities</h2>
    <p class="cap-intro">Field service ( Preventative maintenance and servicing. Breakdowns, Diagnose and repair electrical faults with scan tools. Hydraulic faults. screen media change outs, conveyor belt and roller changes)</p>
    <div class="cap-grid">
      <div class="cap-col">
        <div class="cap-item">Component overhauls ( Engine rebuilds, transmission and final drive rebuilds, hydraulic cylinder reseals, sand pump overhauls, crusher component changes)</div>
        <div class="cap-item">Air conditioning ( Diagnose, service and replacement of all air conditioning components including end of life reclaim and destruction)</div>
        <div class="cap-item">Fabrication ( Heavy fabrication repairs, and hard facing of buckets, rippers and shredders. Fabrication and repairs to fixed plant conveyors, screens and crushers)</div>
      </div>
      <div class="cap-col">
        <div class="cap-item" style="margin-top:40px">Inspections( Pre purchase inspections, BTQLM inspection and reports, wear components and media inspections)</div>
        <div class="cap-item">Line boring (On site line boring including supply and install of pins and bushes)</div>
        <div class="cap-item">Process improvements ( High wear areas, bottle necks, specific gradings and upgrades)</div>
      </div>
    </div>
    <svg class="photo cap-photo" viewBox="0 0 410 170" role="img" aria-label="Photo of a loader under a raised dump body at a quarry site">
      <defs>
        <linearGradient id="site" x1="0" y1="0" x2="0" y2="1">
          <stop offset="0" stop-color="#3d3a33"/>
          <stop offset=".35" stop-color="#5d7fa8"/>
          <stop offset=".6" stop-color="#8a8470"/>
          <stop offset="1" stop-color="#b49c78"/>
        </linearGradient>
      </defs>
      <rect width="410" height="170" fill="url(#site)"/>
    </svg>
    <div class="brand footer-brand"><span class="brand__dot"></span><span class="brand__name">Hallwick<small>Diesel Pty Ltd</small></span></div>
    <span class="footer-bar" style="left:140px;top:540px;width:240px"></span>
    <span class="footer-url" style="left:290px;top:552px">www.yourwebsite.com</span>
    <span class="folio" style="left:378px;top:558px;background:var(--ink);color:#fff">2</span>
  </article>
</section>

</body>
</html>
```